Visitenkarten-Design für eine Zahnarztpraxis
Sehr professionell, sehr kreativ und super freundlich. Vielen Dank!
Zielgruppe
Wir sind eine Zahnarztpraxis mit zwei Standorten und suchen ein neues hochwertiges, modernes und luxuriöses Design.
Aufgabenstellung
Wir haben ein eingetragenes Markenzeichen das sog. 'Zahnbogen'. Bild ist im Anhang. Das Logo vom Zahnbogen (die Kugel) und das Logo auf der Homepage soll nicht verwendet werden. Das Design vom 'Zahnbogen' soll komplett neu gestaltet werden.

```html
<!DOCTYPE html>
<html lang="de">
<head>
<meta charset="utf-8">
<title>Zahnbogen – Visitenkarten</title>
<link href="https://fonts.googleapis.com/css2?family=Montserrat:wght@400;500&family=Poppins:wght@400;500;600&display=swap" rel="stylesheet">
<style>
  :root{
    --navy:#262a66;
    --grey:#5f5f5f;
    --ring:#5a5a5a;
    --ink:#3c3c3c;
    --paper:#ffffff;
    --shadow:rgba(0,0,0,.45);
  }
  *{margin:0;padding:0;box-sizing:border-box}
  html,body{width:1200px;height:738px;overflow:hidden;background:var(--paper)}
  body{position:relative;font-family:"Poppins",sans-serif;color:var(--ink)}

  .brand{position:absolute;left:0;top:46px;width:1200px;text-align:center}
  .brand-ring{display:block;margin:0 auto;width:110px;height:110px;border:4px solid var(--ring);border-radius:50%}
  .brand-name{margin-top:22px;font-family:"Montserrat",sans-serif;font-weight:400;font-size:48px;letter-spacing:2px;color:var(--navy);line-height:1}

  .card{position:absolute;width:269px;height:173px;overflow:hidden;box-shadow:6px 7px 8px var(--shadow)}
  .card-front{display:flex;flex-direction:column;align-items:center;justify-content:center}
  .card-front.grey{background:var(--grey);border-bottom:3px solid var(--navy)}
  .card-front.navy{background:var(--navy);border-bottom:3px solid var(--paper)}
  .front-ring{width:40px;height:40px;border:2px solid var(--paper);border-radius:50%}
  .front-name{margin-top:8px;font-family:"Montserrat",sans-serif;font-size:17px;letter-spacing:1px;color:var(--paper);line-height:1}

  .card-back{background:var(--paper);border-bottom:5px solid var(--grey)}
  .back-arc{position:absolute;left:-28px;top:73px;width:118px;height:118px;border:4px solid var(--ring);border-radius:50%}
  .title{position:absolute;left:16px;top:18px;font-size:6.5px;white-space:nowrap}
  .name-bar{position:absolute;left:0;top:28px;width:94px;height:14px;background:var(--navy);color:var(--paper);font-size:10.5px;font-weight:500;line-height:14px;padding-left:16px;white-space:nowrap;overflow:hidden}
  .role{position:absolute;left:16px;top:46px;font-size:6.5px;white-space:nowrap}
  .info{position:absolute;left:152px;top:26px;font-size:6.3px;line-height:9.4px}
  .info .site{color:var(--navy);font-weight:600}
  .info p+p{margin-top:8px}
  .contact{position:absolute;left:152px;top:127px;font-size:6.3px;line-height:9.6px;list-style:none}
  .contact li{display:flex;align-items:center;gap:3px;white-space:nowrap}
  .contact svg{width:7px;height:7px;flex:none}
</style>
</head>
<body>

<header class="brand">
  <span class="brand-ring"></span>
  <div class="brand-name">ZAHNBOGEN</div>
</header>

<div class="card card-front grey" style="left:265px;top:294px">
  <span class="front-ring"></span>
  <div class="front-name">ZAHNBOGEN</div>
</div>

<div class="card card-front navy" style="left:265px;top:504px">
  <span class="front-ring"></span>
  <div class="front-name">ZAHNBOGEN</div>
</div>

<div class="card card-back" style="left:634px;top:294px">
  <span class="back-arc"></span>
  <div class="title">Dr. med. dent.</div>
  <div class="name-bar">Karim Haddad</div>
  <div class="role">Zahnarzt (D.M.D.)</div>
  <div class="info">
    <p><span class="site">Zahnärzte am Lindenplatz 4</span><br>Am Lindenplatz 4<br>30161 Hannover</p>
    <p><span class="site">Zahn- und Implantatzentrum<br>Waldheim</span><br>Birkenweg 12<br>30895 Waldheim</p>
  </div>
  <ul class="contact">
    <li><svg viewBox="0 0 10 10"><circle cx="5" cy="5" r="5" fill="#262a66"/><path d="M3.3 2.6l1 1-.5.6a4 4 0 0 0 2 2l.6-.5 1 1-.7.8C4.5 7.3 2.7 5.5 2.5 3.3z" fill="#fff"/></svg>0511 000123</li>
    <li><svg viewBox="0 0 10 10"><circle cx="5" cy="5" r="5" fill="#262a66"/><rect x="2.6" y="3.6" width="4.8" height="3.2" fill="#fff"/></svg>0511 000 4567</li>
    <li><svg viewBox="0 0 10 10"><circle cx="5" cy="5" r="5" fill="#262a66"/><rect x="2.5" y="3.2" width="5" height="3.6" fill="#fff"/><path d="M2.5 3.2l2.5 2 2.5-2" stroke="#262a66" stroke-width=".6" fill="none"/></svg>empfang@zlp4.de</li>
    <li><svg viewBox="0 0 10 10"><circle cx="5" cy="5" r="5" fill="#262a66"/><circle cx="5" cy="5" r="2.5" fill="none" stroke="#fff" stroke-width=".7"/></svg>www.zlp4.de</li>
  </ul>
</div>

<div class="card card-back" style="left:634px;top:504px">
  <span class="back-arc"></span>
  <div class="title">Dr. med. dent.</div>
  <div class="name-bar">Karim Haddad</div>
  <div class="role">Zahnarzt (D.M.D.)</div>
  <div class="info">
    <p><span class="site">Zahnärzte am Lindenplatz 4</span><br>Am Lindenplatz 4<br>30161 Hannover</p>
    <p><span class="site">Zahn- und Implantatzentrum<br>Waldheim</span><br>Birkenweg 12<br>30895 Waldheim</p>
  </div>
  <ul class="contact">
    <li><svg viewBox="0 0 10 10"><circle cx="5" cy="5" r="5" fill="#262a66"/><path d="M3.3 2.6l1 1-.5.6a4 4 0 0 0 2 2l.6-.5 1 1-.7.8C4.5 7.3 2.7 5.5 2.5 3.3z" fill="#fff"/></svg>0511 000123</li>
    <li><svg viewBox="0 0 10 10"><circle cx="5" cy="5" r="5" fill="#262a66"/><rect x="2.6" y="3.6" width="4.8" height="3.2" fill="#fff"/></svg>0511 000 4567</li>
    <li><svg viewBox="0 0 10 10"><circle cx="5" cy="5" r="5" fill="#262a66"/><rect x="2.5" y="3.2" width="5" height="3.6" fill="#fff"/><path d="M2.5 3.2l2.5 2 2.5-2" stroke="#262a66" stroke-width=".6" fill="none"/></svg>empfang@zlp4.de</li>
    <li><svg viewBox="0 0 10 10"><circle cx="5" cy="5" r="5" fill="#262a66"/><circle cx="5" cy="5" r="2.5" fill="none" stroke="#fff" stroke-width=".7"/></svg>www.zlp4.de</li>
  </ul>
</div>

</body>
</html>
```